Harmony Swift Care Business card

We want a business card that matches our business theme. Our website is www.swiftcarehub.example
The company name is Harmony Swift Care
The persons having the business cards will be doctors
My logo is attached.
We have a drive-thru medical center where our motto is Fast, Reliable, and Convenient. Our goal is to change the medical space while utilizing technologies, keeping a professional and clean look

Medical

Info on the card should be: Name, Position, Cell number, website, email address, possibly the office line as well

Requirements
Must have
• Logo
Nice to have
• Professional medical feel with our logo colors incorporated

```html
<!DOCTYPE html>
<html lang="en">
<head>
<meta charset="utf-8">
<title>Harmony Swift Care – Business Card</title>
<link rel="stylesheet" href="https://fonts.googleapis.com/css2?family=Arimo:ital,wght@0,400;0,700;1,400;1,700&display=swap">
<style>
  :root {
    --navy: #1e4799;
    --cyan: #40c3f0;
    --white: #ffffff;
    --ink: #111111;
    --stage: #000000;
    --ghost: #eef0f6;
  }
  * { margin: 0; padding: 0; box-sizing: border-box; }
  html, body {
    width: 1007px; height: 1200px; overflow: hidden;
    background: var(--stage);
    font-family: "Arimo", Arial, sans-serif;
  }
  .card {
    position: absolute; left: 51px; width: 905px; height: 503px;
    background: var(--white); overflow: hidden;
  }
  .card--front { top: 51px; }
  .card--back { top: 617px; }
  .card__art { position: absolute; inset: 0; width: 905px; height: 503px; }

  .brand {
    position: absolute; display: flex; align-items: center; gap: 14px;
    color: var(--navy); font-weight: 700; line-height: 1.05;
  }
  .brand__dot { flex: none; border-radius: 50%; background: var(--cyan); }
  .brand--front { left: 34px; top: 40px; font-size: 34px; width: 330px; }
  .brand--front .brand__dot { width: 64px; height: 64px; }
  .brand--back { left: 250px; top: 150px; font-size: 46px; width: 460px; }
  .brand--back .brand__dot { width: 96px; height: 96px; background: var(--navy); }

  .person { position: absolute; left: 0; width: 408px; top: 176px; text-align: center; color: var(--navy); }
  .person__name { font-size: 42px; font-weight: 400; }
  .person__name b { font-weight: 700; }
  .person__role { font-size: 27px; color: var(--ink); margin-top: 4px; letter-spacing: 0.5px; }

  .contact { position: absolute; left: 0; top: 287px; list-style: none; }
  .contact__item {
    display: flex; align-items: center; height: 52px;
    padding-left: 44px; color: var(--white);
    font-size: 26px; font-style: italic; white-space: nowrap;
  }
  .contact__icon {
    width: 40px; height: 40px; border-radius: 50%; background: var(--white);
    display: flex; align-items: center; justify-content: center; margin-right: 24px;
  }
  .contact__icon svg { width: 24px; height: 24px; }

  .tagline { position: absolute; left: 17px; top: 462px; font-size: 20px; font-weight: 700; color: var(--ink); }

  .web {
    position: absolute; color: var(--white); font-style: italic;
    display: flex; align-items: center; white-space: nowrap;
  }
  .web--front { left: 510px; top: 428px; height: 75px; font-size: 25px; }
  .web__globe {
    width: 44px; height: 44px; border-radius: 50%; background: var(--white);
    display: flex; align-items: center; justify-content: center; margin-right: 14px; flex: none;
  }
  .web__globe svg { width: 30px; height: 30px; }
  .web--back { left: 286px; top: 323px; width: 456px; height: 44px; justify-content: center; font-size: 28px; }
</style>
</head>
<body>

<section class="card card--front" aria-label="Front of card">
  <svg class="card__art" viewBox="0 0 531 295" preserveAspectRatio="none" aria-hidden="true">
    <polygon points="283,0 322,0 262,250 200,295 170,295" fill="var(--cyan)"/>
    <g fill="var(--cyan)">
      <rect x="315" y="28" width="160" height="15" rx="7.5"/>
      <rect x="300" y="48" width="130" height="15" rx="7.5"/>
      <rect x="288" y="68" width="112" height="15" rx="7.5"/>
      <rect x="288" y="88" width="140" height="15" rx="7.5"/>
      <rect x="245" y="130" width="40" height="15" rx="7.5"/>
      <rect x="290" y="150" width="165" height="15" rx="7.5"/>
      <rect x="380" y="172" width="120" height="15" rx="7.5"/>
      <rect x="335" y="192" width="135" height="15" rx="7.5"/>
      <rect x="335" y="212" width="165" height="15" rx="7.5"/>
      <rect x="355" y="232" width="110" height="15" rx="7.5"/>
    </g>
    <polygon points="0,160 255,160 278,265 0,265" fill="var(--navy)"/>
    <rect x="210" y="266" width="58" height="17" rx="8.5" fill="var(--white)"/>
    <polygon points="298,250 531,250 531,295 290,295" fill="var(--navy)"/>
  </svg>

  <div class="brand brand--front">
    <span class="brand__dot"></span>
    <span class="brand__name">Harmony Swift Care</span>
  </div>

  <div class="person">
    <h1 class="person__name"><b>Daniel</b> Reyes</h1>
    <p class="person__role">PHYSICIAN</p>
  </div>

  <ul class="contact">
    <li class="contact__item">
      <span class="contact__icon"><svg viewBox="0 0 24 24"><rect x="7" y="2" width="10" height="20" rx="2" fill="var(--navy)"/><rect x="8.5" y="4.5" width="7" height="13" fill="var(--white)"/><circle cx="12" cy="19.6" r="1" fill="var(--white)"/></svg></span>
      (555)-014-2387
    </li>
    <li class="contact__item">
      <span class="contact__icon"><svg viewBox="0 0 24 24"><path d="M3 8c0-3 4-4 9-4s9 1 9 4v2h-5V8H8v2H3z" fill="var(--navy)"/><path d="M7 11h10l3 9H4z" fill="var(--navy)"/><circle cx="12" cy="15" r="2.4" fill="var(--white)"/></svg></span>
      (555)-014-2387
    </li>
    <li class="contact__item">
      <span class="contact__icon"><svg viewBox="0 0 24 24"><rect x="3" y="6" width="18" height="12" fill="var(--navy)"/><path d="M3.5 6.5 12 13l8.5-6.5" stroke="var(--white)" stroke-width="1.5" fill="none"/></svg></span>
      info@swiftcarehub.example
    </li>
  </ul>

  <p class="tagline">Fast \ Reliable \ Convenient</p>

  <div class="web web--front">
    <span class="web__globe"><svg viewBox="0 0 24 24" fill="none" stroke="var(--navy)" stroke-width="1.6"><circle cx="12" cy="12" r="9"/><ellipse cx="12" cy="12" rx="4" ry="9"/><path d="M3 12h18M5 7h14M5 17h14"/></svg></span>
    www.swiftcarehub.example
  </div>
</section>

<section class="card card--back" aria-label="Back of card">
  <svg class="card__art" viewBox="0 0 531 295" preserveAspectRatio="none" aria-hidden="true">
    <polygon points="0,0 300,0 200,295 0,295" fill="var(--cyan)"/>
  </svg>
  <svg class="card__art" viewBox="0 0 531 295" preserveAspectRatio="none" role="img" aria-label="Faint repeating brand pattern area">
    <defs>
      <linearGradient id="ghostFade" x1="0" y1="0" x2="1" y2="1">
        <stop offset="0" stop-color="var(--ghost)"/>
        <stop offset="1" stop-color="var(--white)"/>
      </linearGradient>
    </defs>
    <polygon points="300,0 531,0 531,295 200,295" fill="url(#ghostFade)"/>
  </svg>
  <svg class="card__art" viewBox="0 0 531 295" preserveAspectRatio="none" aria-hidden="true">
    <rect x="168" y="189" width="268" height="26" rx="13" fill="var(--navy)"/>
  </svg>

  <div class="brand brand--back">
    <span class="brand__dot"></span>
    <span class="brand__name">Harmony Swift Care</span>
  </div>

  <div class="web web--back">www.swiftcarehub.example</div>
</section>

</body>
</html>
```